Banner Ad

We need a banner ad for a service. The service is called, "PipeRook" It compiles tweets and Chatterloom posts about state government issues that are posted by U.S. State Legislators. We have a word cloud containing the issues we want to highlight. And we a logo for PipeRook.

The tag is:
Question: Who Is Talking About Issues on Social Media?
Answer: State Legislators
Are you Listening?

The banner ad will be used for print and web. It will go into a regular weekly publication called The Regional Ledger Roundup. http://www.civicpanel-example.com/the-regional-ledger-roundup/

Industry/Entity Type

Government

```html
<!DOCTYPE html>
<html lang="en">
<head>
<meta charset="utf-8">
<title>PipeRook – Are You Listening?</title>
<link rel="stylesheet" href="https://fonts.googleapis.com/css2?family=Saira+Condensed:wght@300;400;700;800&display=swap">
<style>
  :root {
    --navy: #1c2f5e;
    --red: #8e1f2c;
    --cloud-top: #f1f1f3;
    --cloud-bottom: #f7f7f8;
    --paper: #ffffff;
    --stage: #e9e6e1;
  }
  * { margin: 0; padding: 0; box-sizing: border-box; }
  html, body {
    width: 1200px; height: 888px; overflow: hidden;
    background: var(--stage);
  }
  .canvas { position: relative; width: 1200px; height: 888px; overflow: hidden; }
  .ad {
    position: absolute; left: 329px; top: 95px;
    width: 629px; height: 808px;
    transform: scale(0.8665); transform-origin: 0 0;
    background: var(--paper);
    overflow: hidden;
    font-family: "Saira Condensed", sans-serif;
    box-shadow: 0 4px 18px rgba(0,0,0,.18);
  }
  .issue-cloud {
    position: absolute; left: 0; top: 0; width: 100%; height: 679px;
    background: linear-gradient(180deg, var(--cloud-top), var(--cloud-bottom));
  }
  .headline { position: absolute; white-space: nowrap; line-height: 1; }
  .tracked { display: flex; justify-content: space-between; }
  .who { left: 102px; top: 46px; width: 198px; font-size: 120px; font-weight: 400; color: var(--navy); }
  .talking { left: 115px; top: 164px; font-size: 52px; font-weight: 400; color: var(--navy); transform: scaleX(.78); transform-origin: left; }
  .social { left: 301px; top: 218px; font-size: 52px; font-weight: 400; color: var(--navy); transform: scaleX(.78); transform-origin: left; }
  .small-q { left: 505px; top: 166px; font-size: 105px; font-weight: 400; color: var(--navy); transform: scaleX(.7); transform-origin: left; }
  .legislators { left: 53px; top: 285px; font-size: 94px; font-weight: 800; color: var(--navy); letter-spacing: -1px; transform: scaleX(.95); transform-origin: left; }
  .are { left: 102px; top: 443px; width: 116px; font-size: 75px; font-weight: 400; color: var(--navy); }
  .you { left: 232px; top: 426px; width: 223px; font-size: 123px; font-weight: 700; color: var(--navy); }
  .listening { left: 97px; top: 517px; font-size: 116px; font-weight: 400; color: var(--red); transform: scaleX(.98); transform-origin: left; }
  .big-q { left: 482px; top: 411px; font-size: 238px; font-weight: 700; color: var(--red); transform: scaleX(.9); transform-origin: left; }
  .rule { position: absolute; left: 0; width: 100%; }
  .rule-navy { top: 679px; height: 5px; background: var(--navy); }
  .rule-red { top: 685px; height: 6px; background: var(--red); }
  .contact { position: absolute; left: 41px; top: 722px; font-size: 10.5px; line-height: 14px; color: var(--navy); font-weight: 400; }
  .contact .lines { color: var(--red); margin-top: 12px; }
  .brand { position: absolute; left: 397px; top: 728px; display: flex; align-items: center; gap: 10px; }
  .brand-dot { width: 34px; height: 34px; border-radius: 50%; background: var(--red); }
  .brand-name { font-size: 36px; font-weight: 700; color: var(--navy); line-height: 1; }
</style>
</head>
<body>
<div class="canvas">
  <div class="ad">
    <div class="issue-cloud" role="img" aria-label="Faint word cloud of state policy issues behind the headline"></div>

    <div class="headline tracked who"><span>W</span><span>H</span><span>O</span></div>
    <div class="headline talking">Is talking about issues on</div>
    <div class="headline social">Social Media</div>
    <div class="headline small-q">?</div>
    <div class="headline legislators">State Legislators</div>
    <div class="headline tracked are"><span>A</span><span>r</span><span>e</span></div>
    <div class="headline tracked you"><span>Y</span><span>O</span><span>U</span></div>
    <div class="headline listening">Listening</div>
    <div class="headline big-q">?</div>

    <div class="rule rule-navy"></div>
    <div class="rule rule-red"></div>

    <div class="contact">
      <div>1480 Harbor Point Avenue</div>
      <div>6th Floor, Fairlane, Ohio 43017</div>
      <div class="lines">Phone: (555) 014-2290 &nbsp;|&nbsp; Fax: (555) 014-2291 &nbsp;|&nbsp; hello@piperook-example.com</div>
    </div>

    <div class="brand">
      <span class="brand-dot"></span>
      <span class="brand-name">PipeRook</span>
    </div>
  </div>
</div>
</body>
</html>
```